Summer Drinks Flyer for Coffee Shop

We are a coffee shop in London and would like to have a cool and nice flyer for our summer drinks (juices and frozen drink) flyer - see on the attached file for the list

Attached you can find an "attempt" - please note that I would no necessary need the image below.

I also attache our new logo.

thank you

```html
<!DOCTYPE html>
<html lang="en">
<head>
<meta charset="UTF-8">
<title>New Summer Drinks</title>
<link rel="stylesheet" href="https://fonts.googleapis.com/css2?family=Amaranth:ital,wght@0,400;0,700;1,700&family=Chewy&display=swap">
<style>
  :root {
    --white: #ffffff;
    --ink: #2b2420;
    --heading-red: #8e1418;
    --badge-red: #e0262f;
    --title-yellow: #ffdd1f;
    --title-red: #d8201e;
    --gold: #c7a467;
    --brand: #b08a4a;
  }
  * { margin: 0; padding: 0; box-sizing: border-box; }
  html, body { width: 1200px; height: 848px; overflow: hidden; background: var(--white); }
  .flyer {
    position: relative;
    width: 1200px;
    height: 848px;
    overflow: hidden;
    background: var(--white);
    font-family: "Amaranth", sans-serif;
    color: var(--ink);
  }
  .drinks-photo {
    position: absolute;
    left: 0; top: 0;
    width: 563px; height: 848px;
    background:
      linear-gradient(90deg, #6bab2c 0 14%, #8fc24a 24%, #f39a1c 30%, #f6a321 44%, #b8222e 52%, #8a1426 62%, rgba(255,255,255,0) 70%),
      linear-gradient(180deg, #eef2ee 0%, #e4ece7 40%, #f0f2f0 70%, #c8d2d6 88%, #d03a6a 94%, #c9cfd3 100%);
    background-blend-mode: multiply;
  }
  .drinks-photo::after {
    content: "";
    position: absolute; inset: 0;
    background: linear-gradient(90deg, rgba(255,255,255,0) 80%, #ffffff 100%);
  }
  .title {
    position: absolute;
    font-family: "Chewy", cursive;
    color: var(--title-yellow);
    -webkit-text-stroke: 3px var(--title-red);
    paint-order: stroke fill;
    text-shadow: 0 0 0 var(--title-red), 3px 3px 0 var(--title-red), -3px -3px 0 var(--title-red), 3px -3px 0 var(--title-red), -3px 3px 0 var(--title-red), 4px 6px 8px rgba(0,0,0,0.35);
    transform: rotate(-4deg);
    line-height: 1;
    white-space: nowrap;
  }
  .title-new { left: 548px; top: 22px; font-size: 82px; }
  .title-summer { left: 440px; top: 70px; font-size: 116px; }
  .title-drinks { left: 552px; top: 150px; font-size: 80px; }
  .sun-art {
    position: absolute;
    left: 883px; top: 36px;
    width: 292px; height: 178px;
    background: radial-gradient(circle at 62% 50%, #ffd21c 0 30%, #ffb400 42%, rgba(255,180,0,0) 62%);
  }
  .menu { position: absolute; left: 595px; top: 258px; }
  .menu-section { margin-bottom: 22px; }
  .menu-heading {
    font-style: italic;
    font-weight: 700;
    font-size: 27px;
    color: var(--heading-red);
    line-height: 1.2;
    margin-bottom: 2px;
  }
  .menu-items { list-style: none; }
  .menu-items li { font-weight: 700; font-size: 19px; line-height: 26px; }
  .fruit-photo {
    position: absolute;
    left: 960px; top: 363px;
    width: 240px; height: 357px;
    background:
      radial-gradient(ellipse at 65% 40%, #ffc23a 0 28%, rgba(255,194,58,0) 45%),
      radial-gradient(ellipse at 30% 75%, #5fae2e 0 18%, rgba(95,174,46,0) 32%),
      radial-gradient(ellipse at 85% 88%, #e0252c 0 12%, rgba(224,37,44,0) 22%),
      radial-gradient(ellipse at 55% 85%, #f5d23a 0 20%, rgba(245,210,58,0) 34%);
  }
  .badge { position: absolute; }
  .badge-mint { left: 860px; top: 374px; width: 132px; height: 132px; }
  .badge-syrup { left: 848px; top: 567px; width: 114px; height: 114px; }
  .badge text { font-family: "Amaranth", sans-serif; font-weight: 700; fill: var(--white); }
  .divider {
    position: absolute;
    left: 584px; top: 722px;
    width: 616px; height: 2px;
    background: var(--gold);
  }
  .brand {
    position: absolute;
    left: 598px; top: 766px;
    font-family: "Amaranth", sans-serif;
    font-weight: 400;
    font-size: 46px;
    color: var(--brand);
    letter-spacing: 2px;
    line-height: 1;
  }
</style>
</head>
<body>
<main class="flyer">
  <div class="drinks-photo" role="img" aria-label="Three tall glasses of green, orange and red fruit drinks with straws and fruit garnish on a table"></div>

  <h1>
    <span class="title title-new">New</span>
    <span class="title title-summer">Summer</span>
    <span class="title title-drinks">Drinks</span>
  </h1>

  <div class="sun-art" role="img" aria-label="Cartoon sun wearing sunglasses"></div>

  <section class="menu">
    <div class="menu-section">
      <h2 class="menu-heading">Frozen Fruit Drinks</h2>
      <ul class="menu-items">
        <li>Strawberry &amp; banana</li>
        <li>Pineapple, mango &amp; banana</li>
      </ul>
    </div>
    <div class="menu-section">
      <h2 class="menu-heading">Fruit Juices</h2>
      <ul class="menu-items">
        <li>Orange and carrot</li>
        <li>Orange and pineapple</li>
        <li>Pineapple and apple</li>
        <li>Apple and kiwi</li>
        <li>Carrot and ginger</li>
      </ul>
    </div>
    <div class="menu-section">
      <h2 class="menu-heading">Iced-Coffees</h2>
      <ul class="menu-items">
        <li>Iced Coffee</li>
        <li>Iced Latte</li>
        <li>Iced Chocolate Drink</li>
      </ul>
    </div>
  </section>

  <div class="fruit-photo" role="img" aria-label="Glass of orange juice with a straw beside a banana, strawberries and leaves"></div>

  <svg class="badge badge-mint" viewBox="0 0 132 132" aria-label="Add mint or ginger for free">
    <circle cx="66" cy="66" r="64" fill="var(--badge-red)"/>
    <g transform="rotate(-20 66 66)" text-anchor="middle">
      <text x="66" y="42" font-size="17">Add</text>
      <text x="66" y="62" font-size="17">Mint or</text>
      <text x="66" y="82" font-size="17">Ginger for</text>
      <text x="66" y="108" font-size="27">FREE</text>
    </g>
  </svg>

  <svg class="badge badge-syrup" viewBox="0 0 114 114" aria-label="Add syrup shot for 10p, free">
    <circle cx="57" cy="57" r="55" fill="var(--badge-red)"/>
    <g transform="rotate(-20 57 57)" text-anchor="middle">
      <text x="57" y="36" font-size="14">Add</text>
      <text x="57" y="53" font-size="14">Syrup Shot</text>
      <text x="57" y="70" font-size="14">for 10p</text>
      <text x="57" y="93" font-size="23">FREE</text>
    </g>
  </svg>

  <div class="divider"></div>
  <div class="brand">Morbida</div>
</main>
</body>
</html>
```